Your Kid is fantastic Postcards

Korrabin State School
Attached is the one that I did up front and back – this is a postcard for the principal to send to parents about something wonderful their child had done at the school.
We want the mural photo on the front (see attached) with the window blocked out with the words from the principal put there instead. The Postcard will probably have to be long due to the photo as I tried to make one in cardomix and it left half the postcard blank we would ideally have like the A6 size. On the back will need to be as per the back of my sample one. Our website is www.korrabinss.lq.edu.au cheers and thanks
School

```html
<!DOCTYPE html>
<html lang="en">
<head>
<meta charset="utf-8">
<title>Korrabin State School – From the Principal Postcard</title>
<link rel="stylesheet" href="https://fonts.googleapis.com/css2?family=Lobster&family=Roboto+Slab:wght@400&display=swap">
<style>
  :root {
    --backdrop: #b71c26;
    --school-red: #9c1b25;
    --gold: #f2b619;
    --white: #ffffff;
    --ink: #1d1d1d;
    --sky: #5fb8e6;
    --leaf: #4c9a3a;
    --mural-warm: #e6c23a;
  }
  * { margin: 0; padding: 0; box-sizing: border-box; }
  html, body { width: 1200px; height: 852px; overflow: hidden; background: var(--backdrop); }
  .canvas { position: relative; width: 1200px; height: 852px; background: var(--backdrop); }

  .postcard {
    position: absolute; left: 124px; width: 952px; height: 330px;
    box-shadow: 6px 7px 8px rgba(0,0,0,0.35);
    overflow: hidden;
  }
  .postcard--front { top: 74px; }
  .postcard--back { top: 457px; background: var(--white); border: 1px solid var(--gold); }

  .mural {
    position: absolute; inset: 0;
    background:
      linear-gradient(180deg, rgba(76,154,58,0.9) 0%, rgba(95,184,230,0.0) 18%),
      radial-gradient(ellipse at 30% 85%, #e84a3c 0%, rgba(232,74,60,0) 35%),
      radial-gradient(ellipse at 75% 60%, #3fae4a 0%, rgba(63,174,74,0) 30%),
      radial-gradient(ellipse at 62% 40%, var(--mural-warm) 0%, rgba(230,194,58,0) 25%),
      linear-gradient(180deg, var(--sky) 0%, #8fd0d9 50%, #5aa05a 100%);
  }
  .mural--back { right: auto; width: 475px; border-right: 1px solid var(--gold); }

  .title-plate {
    position: absolute; left: 101px; top: 63px; width: 343px; height: 151px;
    background: var(--white); border: 3px solid var(--gold); border-radius: 12px;
    box-shadow: 2px 4px 6px rgba(0,0,0,0.25);
    display: flex; align-items: center;
  }
  .school-mark {
    width: 72px; margin-left: 14px;
    display: flex; flex-direction: column; align-items: center; gap: 4px;
    font-family: "Roboto Slab", serif; font-size: 8px; line-height: 1.15;
    color: var(--school-red); text-align: center;
  }
  .school-mark__dot { width: 14px; height: 14px; border-radius: 50%; background: var(--school-red); }
  .title-plate__rule { width: 2px; height: 84px; background: var(--gold); margin: 0 14px 0 8px; }
  .title-plate__lead { font-family: "Roboto Slab", serif; font-size: 18px; color: var(--ink); }
  .title-plate__heading {
    font-family: "Lobster", cursive; font-size: 66px; line-height: 0.9;
    color: var(--school-red); font-weight: 400;
  }

  .message-panel {
    position: absolute; left: 28px; top: 47px; width: 404px; height: 257px;
    background: rgba(255,255,255,0.78); border-radius: 12px;
    font-family: "Roboto Slab", serif; font-size: 16px; color: var(--ink);
    padding: 0 0 0 43px;
  }
  .message-panel__greeting { position: absolute; top: 32px; left: 43px; }
  .message-panel__greeting-line {
    position: absolute; top: 47px; left: 80px; width: 268px; height: 1.5px; background: var(--gold);
  }
  .message-panel__body { position: absolute; top: 80px; left: 43px; width: 330px; line-height: 1.28; }
  .message-panel__signoff { position: absolute; top: 228px; left: 43px; white-space: nowrap; }
  .message-panel__signature { font-family: "Lobster", cursive; font-size: 24px; color: var(--school-red); margin-left: 4px; }

  .stamp-box { position: absolute; left: 840px; top: 20px; width: 91px; height: 90px; border: 1.5px solid var(--gold); }
  .address-lines { position: absolute; left: 515px; top: 110px; width: 302px; }
  .address-lines span { display: block; height: 1.5px; background: var(--gold); margin-bottom: 29px; }

  .school-mark--back {
    position: absolute; left: 830px; top: 238px; width: 110px; font-size: 13px; gap: 6px;
  }
  .school-mark--back .school-mark__dot { width: 22px; height: 22px; }
</style>
</head>
<body>
<main class="canvas">

  <section class="postcard postcard--front">
    <div class="mural" role="img" aria-label="Colourful school playground mural with a kookaburra, a crocodile, an echidna, a butterfly, speech bubbles and painted school lettering"></div>
    <div class="title-plate">
      <div class="school-mark">
        <span class="school-mark__dot"></span>
        <span>Korrabin State School</span>
      </div>
      <span class="title-plate__rule"></span>
      <div>
        <p class="title-plate__lead">From the</p>
        <h1 class="title-plate__heading">Principal</h1>
      </div>
    </div>
  </section>

  <section class="postcard postcard--back">
    <div class="mural mural--back" role="img" aria-label="Close-up of the school mural with a crocodile, an echidna and speech bubbles"></div>
    <div class="message-panel">
      <p class="message-panel__greeting">Dear</p>
      <span class="message-panel__greeting-line"></span>
      <p class="message-panel__body">This postcard is to let you know how proud I am that</p>
      <p class="message-panel__signoff">Yours in education,<span class="message-panel__signature">Ms. Verity</span></p>
    </div>
    <div class="stamp-box"></div>
    <div class="address-lines"><span></span><span></span><span></span><span></span><span></span></div>
    <div class="school-mark school-mark--back">
      <span class="school-mark__dot"></span>
      <span>Korrabin State School</span>
    </div>
  </section>

</main>
</body>
</html>
```